Acupuncture Medspa needs a business card design

I need a business card design that looks professional, has a spa-like quality and can offer a promo on the back. Initial promo is "First session free". The tagline of NeedleNook is: Refresh, Restore, Rejuvenate.

NeedleNook is a membership-based acupuncture medspa that offers acupuncture, cupping, and herbal therapies. Members choose between the "Refresh" membership which is for stress relief, or "Restore" which is for treating health conditions, and lastly "Rejuvenate" which is for natural facial enhancement.

Industry/Entity Type

Health And Wellness

Contact Information for Business Card

Coral Haskins, MAC, L.Ac.
612-555-0193
www.needlenook-example.com

Font styles to use
Serif
Sans Serif

Colors

Designer to choose colors to be used in the design.

Requirements
Must have
• The project must have NeedleNook logo, promo on the back, and contact information
Nice to have
• I would like to see the colors of the logo used.

```html
<!DOCTYPE html>
<html lang="en">
<head>
<meta charset="utf-8">
<title>NeedleNook Business Card</title>
<link rel="stylesheet" href="https://fonts.googleapis.com/css2?family=Lato:wght@400;700&family=Open+Sans:wght@400;700&display=swap">
<style>
  :root {
    --bg: #dcdbd8;
    --paper: #ffffff;
    --teal: #138c84;
    --teal-light: #1d968e;
    --mint: #b8dedc;
    --mint-faint: #e6f2f1;
    --ink: #3a1f14;
    --text: #2b2b2b;
  }
  * { box-sizing: border-box; margin: 0; padding: 0; }
  html, body { width: 1200px; height: 801px; overflow: hidden; }
  body {
    background: var(--bg);
    display: flex;
    align-items: center;
    justify-content: center;
    gap: 50px;
    font-family: "Open Sans", sans-serif;
  }
  .card {
    position: relative;
    width: 520px;
    height: 297px;
    overflow: hidden;
    box-shadow: 0 6px 18px rgba(0,0,0,0.18);
  }

  /* Front */
  .card--front { background: var(--paper); }
  .front__accent {
    position: absolute;
    right: -70px;
    top: -120px;
    width: 300px;
    height: 300px;
    border-radius: 50%;
    border: 9px solid var(--mint-faint);
  }
  .brand {
    font-family: "Lato", sans-serif;
    font-weight: 700;
    letter-spacing: 0.04em;
    text-transform: uppercase;
    display: flex;
    align-items: center;
  }
  .brand__dot {
    display: inline-block;
    border-radius: 50%;
  }
  .front__brand {
    position: absolute;
    left: 40px;
    top: 78px;
    color: var(--teal);
    font-size: 30px;
    gap: 10px;
  }
  .front__brand .brand__dot {
    width: 22px; height: 22px;
    border: 3px solid var(--teal);
  }
  .person {
    position: absolute;
    left: 40px;
    top: 150px;
  }
  .person__name {
    font-weight: 700;
    font-size: 18px;
    color: var(--ink);
  }
  .person__creds {
    font-family: "Lato", sans-serif;
    font-weight: 700;
    font-size: 13px;
    color: var(--teal);
    margin-top: 2px;
  }
  .contact {
    list-style: none;
    margin-top: 14px;
    font-size: 12.5px;
    color: var(--text);
    line-height: 1.65;
  }
  .contact__label {
    display: inline-block;
    width: 22px;
    color: var(--teal);
    font-weight: 700;
  }

  /* Back */
  .card--back {
    background: linear-gradient(160deg, var(--teal-light) 0%, var(--teal) 60%);
    color: #fff;
  }
  .back__brand {
    position: absolute;
    left: 0; right: 0;
    top: 70px;
    justify-content: center;
    font-size: 46px;
    gap: 14px;
    color: #fff;
  }
  .back__brand .brand__dot {
    width: 42px; height: 42px;
    border: 4px solid #fff;
  }
  .promo {
    position: absolute;
    left: 0; right: 0;
    top: 168px;
    text-align: center;
    font-family: "Lato", sans-serif;
    font-size: 17px;
    letter-spacing: 0.05em;
  }
  .tagline {
    position: absolute;
    left: 0; right: 0;
    bottom: 16px;
    height: 52px;
    background: var(--mint);
    display: flex;
    justify-content: space-around;
    align-items: center;
    list-style: none;
    font-family: "Lato", sans-serif;
    font-size: 17px;
    letter-spacing: 0.04em;
    color: var(--teal);
  }
</style>
</head>
<body>
  <section class="card card--front" aria-label="Business card front">
    <div class="front__accent" aria-hidden="true"></div>
    <div class="brand front__brand"><span class="brand__dot" aria-hidden="true"></span>NeedleNook</div>
    <div class="person">
      <p class="person__name">Coral Haskins</p>
      <p class="person__creds">MAC, L.AC</p>
      <ul class="contact">
        <li><span class="contact__label">T:</span>612-555-0193</li>
        <li><span class="contact__label">E:</span>info@needlenook-example.com</li>
        <li><span class="contact__label">W:</span>www.needlenook-example.com</li>
      </ul>
    </div>
  </section>

  <section class="card card--back" aria-label="Business card back">
    <div class="brand back__brand"><span class="brand__dot" aria-hidden="true"></span>NeedleNook</div>
    <p class="promo">FIRST SESSION FREE</p>
    <ul class="tagline">
      <li>REFRESH</li>
      <li>RESTORE</li>
      <li>REJUVENATE</li>
    </ul>
  </section>
</body>
</html>
```